Briefing for design project – two page infographic to sit within a newspaper spread

We need a two page camera ready graphic design insert to go into a national quality newspaper, the Wollondale Ledger, that tells the story of the value of sports, recreation, the arts and tourism in the lives of people with disability, the ways that people are disconnected from these opportunities due to barriers and lack of supports; and describe how social and economic participation are linked.

The infographic should tell a compelling story - we will provide the statistics and information and the designer will need to tell the story. We will need you to liaise via us with the newspaper to ensure the product is delivered within design specs.

```html
<!DOCTYPE html>
<html lang="en">
<head>
<meta charset="utf-8">
<title>Disability, Sport and the Arts – Wollondale Ledger Insert</title>
<link href="https://fonts.googleapis.com/css2?family=Bebas+Neue&family=Didact+Gothic&display=swap" rel="stylesheet">
<style>
  :root {
    --paper: #f8f8f8;
    --ink: #1b1b1b;
    --teal: #0d7f80;
    --rule: #1b1b1b;
  }
  * { margin: 0; padding: 0; box-sizing: border-box; }
  html, body { width: 1200px; height: 1000px; overflow: hidden; background: var(--paper); }
  .canvas { position: relative; width: 1200px; height: 1000px; background: var(--paper); color: var(--ink); font-family: "Didact Gothic", "Century Gothic", sans-serif; }
  .rule { position: absolute; height: 4px; background: var(--rule); }
  .rule--left { left: 0; width: 595px; }
  .rule--right { left: 648px; width: 552px; }
  .pictogram { position: absolute; background: var(--ink); border-radius: 6px; }
  .pictogram--teal { background: linear-gradient(180deg, var(--ink) 0%, var(--ink) 60%, var(--teal) 100%); }
  .figure { position: absolute; font-family: "Bebas Neue", "Oswald", sans-serif; color: var(--teal); line-height: 1; letter-spacing: 0.5px; }
  .figure small { font-size: 0.5em; }
  .caption { position: absolute; font-size: 19px; line-height: 16px; color: var(--ink); white-space: nowrap; }
  .caption--lead { font-size: 20px; line-height: 17px; }
  .caption em { font-style: normal; color: var(--teal); }
  .aside { position: absolute; font-size: 16px; line-height: 1; color: var(--ink); }
</style>
</head>
<body>
<main class="canvas">
  <div class="rule rule--left" style="top:36px"></div>
  <div class="rule rule--left" style="top:168px"></div>
  <div class="rule rule--left" style="top:269px"></div>
  <div class="rule rule--left" style="top:548px"></div>
  <div class="rule rule--left" style="top:727px"></div>
  <div class="rule rule--right" style="top:36px"></div>
  <div class="rule rule--right" style="top:324px"></div>
  <div class="rule rule--right" style="top:521px"></div>

  <section class="stat stat--prevalence">
    <div class="pictogram" role="img" aria-label="Row of five person pictograms, one using crutches" style="left:40px;top:55px;width:228px;height:97px;"></div>
    <div class="figure" style="left:278px;top:80px;font-size:56px;">1<small>in</small>5</div>
    <p class="caption caption--lead" style="left:279px;top:131px;">Australians have a disability</p>
  </section>

  <section class="stat stat--territory">
    <div class="figure" style="left:48px;top:190px;font-size:56px;">57,500</div>
    <div class="pictogram" role="img" aria-label="Wheelchair user pictogram" style="left:150px;top:193px;width:32px;height:45px;background:transparent;border:3px solid var(--teal);"></div>
    <p class="caption caption--lead" style="left:187px;top:220px;">living in the ACT have a disability</p>
  </section>

  <section class="stat stat--sport">
    <div class="pictogram" role="img" aria-label="Pictogram of a person shooting a basketball" style="left:40px;top:285px;width:80px;height:133px;"></div>
    <div class="figure" style="left:30px;top:420px;font-size:64px;">65%</div>
    <p class="caption" style="left:32px;top:474px;">of Australians<br>participate<br>in sport</p>

    <div class="pictogram" role="img" aria-label="Pictogram of a person throwing a ball" style="left:232px;top:318px;width:86px;height:100px;"></div>
    <div class="figure" style="left:222px;top:420px;font-size:64px;">49%</div>
    <p class="caption" style="left:224px;top:474px;">of Australians<br>with a moderate<br>or mild disability<br>participate in sport</p>

    <div class="pictogram" role="img" aria-label="Pictogram of a wheelchair basketball player" style="left:420px;top:328px;width:85px;height:90px;"></div>
    <div class="figure" style="left:413px;top:420px;font-size:64px;">35%</div>
    <p class="caption" style="left:415px;top:474px;">of Australians<br>with a more<br>significant disability<br>participate in sport</p>
  </section>

  <section class="stat stat--arts">
    <div class="figure" style="left:22px;top:585px;font-size:64px;">25%</div>
    <div class="pictogram pictogram--teal" role="img" aria-label="Theatre comedy and tragedy masks" style="left:192px;top:570px;width:88px;height:72px;"></div>
    <p class="caption" style="left:26px;top:641px;">of people with disability<br>attended theatres or<br>concerts, compared with<br>a <em>38%</em> of all Australians</p>

    <div class="pictogram pictogram--teal" role="img" aria-label="Silhouette of a classical statue" style="left:318px;top:585px;width:46px;height:122px;"></div>
    <div class="figure" style="left:370px;top:585px;font-size:64px;">20%</div>
    <p class="caption" style="left:373px;top:641px;">of people with disability<br>visited museums or art-<br>galleries, compared with<br>a <em>32%</em> of all Australians</p>
  </section>

  <section class="stat stat--medals">
    <div class="pictogram" role="img" aria-label="Para games medal hanging from a ribbon" style="left:675px;top:38px;width:75px;height:262px;border-radius:0 0 38px 38px;"></div>
    <div class="pictogram" role="img" aria-label="Summer games medal hanging from a ribbon" style="left:766px;top:38px;width:80px;height:182px;border-radius:0 0 40px 40px;"></div>
    <div class="figure" style="left:850px;top:150px;font-size:56px;">35</div>
    <p class="caption caption--lead" style="left:853px;top:204px;">medals were won by Australia<br>in Harbourvale Summer Games 2012</p>
    <p class="aside" style="left:765px;top:226px;">while</p>
    <div class="figure" style="left:757px;top:238px;font-size:56px;">85</div>
    <p class="caption caption--lead" style="left:761px;top:288px;">medals were won in the Harbourvale Para Games</p>
  </section>

  <section class="stat stat--isolation">
    <div class="pictogram" role="img" aria-label="Pictogram of a weightlifter raising a barbell" style="left:678px;top:365px;width:127px;height:34px;"></div>
    <div class="pictogram" aria-hidden="true" style="left:728px;top:399px;width:29px;height:88px;border-radius:0 0 4px 4px;"></div>
    <p class="aside" style="left:795px;top:410px;">over</p>
    <div class="figure" style="left:757px;top:424px;font-size:64px;">37,000</div>
    <p class="caption caption--lead" style="left:828px;top:473px;">people with disability don't get out at all</p>
  </section>
</main>
</body>
</html>
```